Business Cards for Tomas and Welby

Design of business cards for two people with the recently created brand Caldor Mobile. Caldor Mobile wants to become a worldwide major player on the secondhand phone market. It gathers send hand phones from individuals, refurbish them and sell them throughout the world. It has a green impact (recycling) and we also contribute to social project in Africa (a percentage of our benefits are sent to build school, sport facilities, etc.

Target Market(s)

B2B - Tomas and Welby are in contact with distributors across Africa.

Industry/Entity Type

Wireless Communication

Contact Information for Business Card

Tomas Vireaux
Head of Emerging Markets
Caldor Energy South Africa (Pty) Ltd
Fennick Street 47
2031 Sandton - Johannesburg
South Africa
Tel: + 27 10 555 0184
Mobile : +27 82 55 017
Email : tomas.vireaux@caldormobile.example
Skype: tomas.vireaux
Web: www.caldormobile.example
 

Welby Crofts
Head of Southern Africa
Fennick Street 47
South Africa
Tel: + 27 10 555 0184
Mobile: +27 83 555 0297
Email: welby.crofts@caldormobile.example
Skype: welby.crofts
Web: www.caldormobile.example

Requirements
Must have
• The cards need to be "serious", trustable, with a worldwide presence.
Nice to have
• Some "green" / recycling touch would be nice but not necessary if in contradiction with the general design.

```html
<!DOCTYPE html>
<html lang="en">
<head>
<meta charset="utf-8">
<title>Caldor Mobile – Business Cards</title>
<link rel="stylesheet" href="https://fonts.googleapis.com/css2?family=Open+Sans:wght@400;600;700&display=swap">
<style>
  :root {
    --backdrop: #3a302b;
    --card: #121212;
    --card-edge: #1c1c1c;
    --brand-blue: #2e95dc;
    --brand-deep: #1d5b8c;
    --text-light: #f2f2f2;
  }
  * { box-sizing: border-box; margin: 0; padding: 0; }
  html, body {
    width: 1200px; height: 844px; overflow: hidden;
    background: var(--backdrop);
    font-family: "Open Sans", Arial, sans-serif;
  }
  .stage {
    position: relative; width: 1200px; height: 844px;
    display: flex; align-items: center; justify-content: center; gap: 50px;
  }
  .card {
    position: relative; width: 525px; height: 300px;
    background: var(--card);
    border: 1px solid var(--card-edge);
    box-shadow: 0 12px 30px rgba(0,0,0,.45);
  }
  /* contact side */
  .identity { position: absolute; left: 34px; top: 120px; }
  .person-name { color: var(--brand-blue); font-weight: 700; font-size: 19px; line-height: 24px; }
  .person-role { color: var(--text-light); font-size: 13px; line-height: 19px; margin-top: 2px; }
  .company { color: var(--brand-blue); font-weight: 600; font-size: 13px; line-height: 19px; margin-top: 22px; }
  .address { color: var(--text-light); font-size: 13px; line-height: 20px; margin-top: 2px; }
  .contacts {
    position: absolute; right: 30px; top: 96px;
    list-style: none; text-align: right;
  }
  .contacts li {
    display: flex; justify-content: flex-end; align-items: center; gap: 8px;
    color: var(--text-light); font-size: 13px; line-height: 22px;
  }
  .contacts svg { width: 12px; height: 12px; flex: none; }
  /* brand side */
  .brand {
    position: absolute; inset: 0;
    display: flex; align-items: center; justify-content: center; gap: 14px;
  }
  .brand-dot { width: 26px; height: 26px; border-radius: 50%; background: var(--brand-blue); }
  .brand-name { color: var(--brand-deep); font-weight: 700; font-size: 36px; letter-spacing: -0.5px; }
</style>
</head>
<body>
<main class="stage">
  <section class="card card-contact" aria-label="Contact side">
    <div class="identity">
      <p class="person-name">Tomas Vireaux</p>
      <p class="person-role">Head of Emerging Markets</p>
      <p class="company">Caldor Energy South Africa (Pty) Ltd</p>
      <p class="address">Fennick Street 47 2031<br>Sandton - Johannesburg South Africa</p>
    </div>
    <ul class="contacts">
      <li>+ 27 10 555 0184
        <svg viewBox="0 0 12 12" aria-hidden="true"><path d="M2.5 1l2 2.2-1 1.3a6 6 0 0 0 4 4l1.3-1 2.2 2-1.2 1.5C5.5 11 1 6.5 1 2.2z" fill="var(--brand-blue)"/></svg></li>
      <li>+27 82 55 017
        <svg viewBox="0 0 12 12" aria-hidden="true"><rect x="3" y="0.5" width="6" height="11" rx="1" fill="none" stroke="var(--brand-blue)" stroke-width="1.3"/><circle cx="6" cy="9.6" r=".7" fill="var(--brand-blue)"/></svg></li>
      <li>tomas.vireaux@caldormobile.example
        <svg viewBox="0 0 12 12" aria-hidden="true"><rect x="0.5" y="2.5" width="11" height="7.5" fill="var(--brand-blue)"/><path d="M0.5 2.5l5.5 4 5.5-4" fill="none" stroke="var(--card)" stroke-width="1"/></svg></li>
      <li>www.caldormobile.example
        <svg viewBox="0 0 12 12" aria-hidden="true"><circle cx="6" cy="6" r="5.3" fill="var(--brand-blue)"/><path d="M1 6h10M6 .8c-2.5 3-2.5 7.4 0 10.4M6 .8c2.5 3 2.5 7.4 0 10.4" fill="none" stroke="var(--card)" stroke-width=".8"/></svg></li>
      <li>tomas.vireaux
        <svg viewBox="0 0 12 12" aria-hidden="true"><circle cx="6" cy="6" r="5.3" fill="var(--brand-blue)"/></svg></li>
    </ul>
  </section>

  <section class="card card-brand" aria-label="Brand side">
    <div class="brand">
      <span class="brand-dot" aria-hidden="true"></span>
      <span class="brand-name">Caldor Mobile</span>
    </div>
  </section>
</main>
</body>
</html>
```